Looking for a modern, Professional business card design

We have a simple business card, but are looking for a more modern, professional look. A sample of the basic card is attached as well as the logo. We would also like to add that we offer:
Struggling with your finances?
- Learn to become debt free
- Discover the power of cash
- Control your money instead of it controlling you
Let us help you achieve a new level of financial freedom!
Also, we would like to have a "SPECIAL OFFER!: FREE 30 minute consultation"
Financial Planning

```html
<!DOCTYPE html>
<html lang="en">
<head>
<meta charset="utf-8">
<title>Brightpath Financial Coaching – Business Card</title>
<link href="https://fonts.googleapis.com/css2?family=Josefin+Sans:wght@400;600;700&family=Russo+One&display=swap" rel="stylesheet">
<style>
  :root {
    --bg: #2b2b2b;
    --green-deep: #3a8f3f;
    --green-mid: #45a047;
    --green-bright: #6cc04a;
    --green-lime: #9bd23c;
    --ink: #1a1a1a;
    --paper: #ffffff;
  }
  * { box-sizing: border-box; margin: 0; padding: 0; }
  html, body { width: 1200px; height: 900px; overflow: hidden; }
  body {
    background: var(--bg);
    font-family: "Josefin Sans", sans-serif;
    position: relative;
  }
  .card {
    position: absolute;
    width: 620px;
    height: 354px;
    border-radius: 22px;
    overflow: hidden;
    box-shadow: 0 14px 30px rgba(0,0,0,.45);
  }

  /* ---------- Front ---------- */
  .card-front {
    left: 90px; top: 70px;
    background: var(--green-deep);
    color: var(--paper);
  }
  .front-brand {
    position: absolute; left: 190px; top: 34px;
    display: flex; align-items: center; gap: 12px;
  }
  .brand-dot {
    width: 26px; height: 26px; border-radius: 50%;
    background: var(--green-lime);
    flex: none;
  }
  .front-brand .brand-name {
    font-family: "Josefin Sans", sans-serif;
    font-weight: 700;
    font-size: 40px;
    letter-spacing: 1px;
    color: var(--ink);
    line-height: 1;
  }
  .front-brand .brand-sub {
    font-weight: 700; font-size: 15px; letter-spacing: 1px;
    color: var(--green-lime); margin-top: 4px;
  }
  .front-brand .brand-tagline {
    font-size: 10px; color: var(--paper); margin-top: 2px;
  }
  .pitch {
    position: absolute; left: 44px; top: 150px;
  }
  .pitch-heading {
    font-weight: 600; font-size: 21px; letter-spacing: 1.5px;
    text-transform: uppercase;
  }
  .accent { color: var(--green-lime); }
  .pitch-list { list-style: none; margin-top: 8px; }
  .pitch-list li {
    font-size: 19px; line-height: 1.35; padding-left: 22px; position: relative;
  }
  .pitch-list li::before {
    content: ""; position: absolute; left: 2px; top: 7px;
    width: 10px; height: 10px; border-radius: 50%;
    background: var(--green-lime);
  }
  .call-to-action {
    position: absolute; left: 0; right: 0; top: 268px;
    text-align: center; font-size: 17px; line-height: 1.3;
    text-transform: uppercase; letter-spacing: .5px;
  }
  .front-edge {
    position: absolute; left: 0; right: 0; bottom: 0; height: 12px;
    background: var(--green-bright);
  }
  .front-notch {
    position: absolute; left: 330px; width: 190px; bottom: 0; height: 12px;
    background: var(--paper);
  }

  /* ---------- Back ---------- */
  .card-back {
    left: 490px; top: 470px;
    background: var(--paper);
    color: var(--ink);
  }
  .back-mark {
    position: absolute; left: 36px; top: 120px;
    display: flex; align-items: center; gap: 12px;
  }
  .back-mark .brand-dot { width: 30px; height: 30px; background: var(--green-bright); }
  .back-mark .brand-name {
    font-weight: 700; font-size: 36px; color: var(--green-mid);
  }
  .contact {
    position: absolute; left: 330px; top: 50px;
  }
  .person-name {
    font-family: "Russo One", sans-serif; font-size: 22px; letter-spacing: 1px;
    text-transform: uppercase;
  }
  .person-role {
    font-family: "Russo One", sans-serif; font-size: 13px; letter-spacing: 2px;
    color: var(--green-mid); text-transform: uppercase; margin-top: 4px;
  }
  .contact-list { list-style: none; margin-top: 14px; }
  .contact-list li {
    display: flex; align-items: center; gap: 10px;
    font-size: 16px; line-height: 1.6; color: var(--green-mid);
  }
  .contact-icon { width: 18px; height: 18px; flex: none; }
  .offer {
    position: absolute; left: 330px; top: 238px;
  }
  .offer-title {
    font-family: "Russo One", sans-serif; font-size: 18px; letter-spacing: 5px;
  }
  .offer-detail {
    font-weight: 700; font-size: 14px; color: var(--green-mid); margin-top: 2px;
  }
  .back-band {
    position: absolute; left: 0; right: 0; bottom: 0; height: 16px;
    background: linear-gradient(90deg, var(--green-bright), var(--green-lime));
  }
  .back-band-accent {
    position: absolute; left: 330px; right: 0; bottom: 16px; height: 10px;
    background: var(--green-mid);
  }
</style>
</head>
<body>

<section class="card card-front">
  <div class="front-brand">
    <span class="brand-dot"></span>
    <div>
      <div class="brand-name">BRIGHTPATH</div>
      <div class="brand-sub">FINANCIAL COACHING</div>
      <div class="brand-tagline">Achieve a new level of personal freedom</div>
    </div>
  </div>

  <div class="pitch">
    <h2 class="pitch-heading">Struggling with your <span class="accent">finances?</span></h2>
    <ul class="pitch-list">
      <li>Learn to become debt free</li>
      <li>Discover the power of cash</li>
      <li>Control your money instead of it controlling you</li>
    </ul>
  </div>

  <p class="call-to-action">Let us help you<br>Achieve a new level of <span class="accent">financial freedom!</span></p>

  <div class="front-edge"></div>
  <div class="front-notch"></div>
</section>

<section class="card card-back">
  <div class="back-mark">
    <span class="brand-dot"></span>
    <span class="brand-name">Brightpath</span>
  </div>

  <div class="contact">
    <h1 class="person-name">Daniel R. Hayes</h1>
    <p class="person-role">Personal Financial Coach</p>
    <ul class="contact-list">
      <li>
        <svg class="contact-icon" viewBox="0 0 18 18"><circle cx="9" cy="9" r="9" fill="#45a047"/><rect x="6" y="4" width="6" height="10" rx="1.2" fill="none" stroke="#fff" stroke-width="1.4"/></svg>
        555-0148 (205)
      </li>
      <li>
        <svg class="contact-icon" viewBox="0 0 18 18"><circle cx="9" cy="9" r="9" fill="#45a047"/><rect x="4.5" y="6" width="9" height="6.5" fill="none" stroke="#fff" stroke-width="1.3"/><path d="M4.5 6 L9 10 L13.5 6" fill="none" stroke="#fff" stroke-width="1.3"/></svg>
        daniel@brightpathmoney.com
      </li>
      <li>
        <svg class="contact-icon" viewBox="0 0 18 18"><circle cx="9" cy="9" r="9" fill="#45a047"/><circle cx="9" cy="9" r="4.5" fill="none" stroke="#fff" stroke-width="1.2"/><path d="M4.5 9 H13.5 M9 4.5 C7 7 7 11 9 13.5 M9 4.5 C11 7 11 11 9 13.5" fill="none" stroke="#fff" stroke-width="1"/></svg>
        www.brightpathmoney.com
      </li>
    </ul>
  </div>

  <div class="offer">
    <p class="offer-title">SPECIAL OFFER!</p>
    <p class="offer-detail">FREE 30 minute consultation</p>
  </div>

  <div class="back-band-accent"></div>
  <div class="back-band"></div>
</section>

</body>
</html>
```